Copper Kettle Catering
Business Cards and Letterhead
Copper Kettle Catering -
Creative Brief
Use standard fonts
R Danela Forsythe
Chef/Owner
287 W 93rd St FL2 New York, NY 10025
copperkettlecatering@mailbox.example
copperkettlecatering.example

```html
<!DOCTYPE html>
<html lang="en">
<head>
<meta charset="utf-8">
<title>Copper Kettle Catering – Business Card</title>
<link href="https://fonts.googleapis.com/css2?family=Open+Sans:wght@400;600;700&display=swap" rel="stylesheet">
<style>
  :root {
    --backdrop: #cfcfcf;
    --card: #ffffff;
    --brand-red: #d8262b;
    --brand-orange: #f0a33a;
    --ink: #4a4a4a;
    --ink-soft: #6b6b6b;
  }
  * { box-sizing: border-box; margin: 0; padding: 0; }
  html, body { width: 1200px; height: 403px; overflow: hidden; }
  body {
    background: var(--backdrop);
    font-family: "Open Sans", Arial, sans-serif;
    position: relative;
  }
  .card {
    position: absolute;
    top: 24px;
    width: 567px;
    height: 355px;
    background: var(--card);
    border-radius: 22px;
    overflow: hidden;
    box-shadow: 0 1px 3px rgba(0,0,0,.15);
  }
  .card--front { left: 19px; }
  .card--back { left: 617px; }

  .brand-name {
    position: absolute;
    left: 0; right: 0;
    text-align: center;
    color: var(--brand-orange);
    font-weight: 600;
    line-height: 1;
  }
  .card--front .brand-name { top: 72px; font-size: 26px; }
  .card--back .brand-name { top: 148px; font-size: 40px; }

  .band { position: absolute; left: 0; top: 150px; width: 567px; height: 100px; }
  .identity {
    position: absolute;
    top: 190px; left: 0; right: 0;
    text-align: center;
    color: #fff;
    font-size: 15px;
    font-weight: 700;
  }
  .identity .divider { font-weight: 400; margin: 0 10px; }
  .identity .role { font-weight: 600; font-size: 13px; }

  .address {
    position: absolute;
    top: 254px; left: 0; right: 0;
    text-align: center;
    font-size: 12px;
    color: var(--ink);
  }
  .contacts {
    position: absolute;
    top: 282px; left: 70px; right: 20px;
    display: flex;
    flex-wrap: wrap;
    column-gap: 14px;
    row-gap: 10px;
    font-size: 11.5px;
    color: var(--ink);
  }
  .contact { display: flex; align-items: center; gap: 5px; white-space: nowrap; }
  .contact svg { width: 11px; height: 11px; flex: none; }
  .contact--web { width: 100%; }

  .web-back {
    position: absolute;
    top: 320px; left: 0; right: 0;
    text-align: center;
    font-size: 13px;
    font-weight: 600;
    color: var(--ink-soft);
    letter-spacing: .5px;
  }
</style>
</head>
<body>
  <section class="card card--front">
    <div class="brand-name">Copper Kettle Catering</div>

    <svg class="band" viewBox="0 0 567 100" preserveAspectRatio="none" aria-hidden="true">
      <path d="M0 22 C150 -8 380 48 567 10 L567 78 C400 100 170 60 0 88 Z" fill="var(--brand-red)"/>
      <path d="M0 94 C170 66 400 104 567 84" fill="none" stroke="var(--brand-orange)" stroke-width="3"/>
    </svg>

    <p class="identity">R Danela Forsythe<span class="divider">|</span><span class="role">Chef/Owner</span></p>
    <p class="address">287 W 93rd St FL2 New York, NY 10025</p>

    <div class="contacts">
      <span class="contact">
        <svg viewBox="0 0 12 12"><path d="M3 1 L5 3.5 L4 5 C5 7 6 8 7.5 8.5 L9 7.5 L11 9.5 L9.5 11 C5 11 1 7 1 2.5 Z" fill="var(--brand-red)"/></svg>
        347.555.0142
      </span>
      <span class="contact">
        <svg viewBox="0 0 12 12"><circle cx="6" cy="6" r="6" fill="var(--brand-red)"/><path d="M4.5 3 L5.5 4.5 L5 5.3 C5.5 6.3 6 6.8 6.8 7.1 L7.5 6.6 L9 7.6 L8.2 8.7 C5.6 8.7 3.5 6.6 3.4 4 Z" fill="#fff"/></svg>
        347.555.0187
      </span>
      <span class="contact">
        <svg viewBox="0 0 12 12"><circle cx="6" cy="6" r="6" fill="var(--brand-red)"/><rect x="3" y="4" width="6" height="4.2" fill="#fff"/><path d="M3 4 L6 6.4 L9 4" fill="none" stroke="var(--brand-red)" stroke-width=".8"/></svg>
        copperkettlecatering@mailbox.example
      </span>
      <span class="contact contact--web">
        <svg viewBox="0 0 12 12"><circle cx="6" cy="6" r="6" fill="var(--brand-red)"/><circle cx="6" cy="6" r="3" fill="none" stroke="#fff" stroke-width="1"/><path d="M3 6 H9 M6 3 V9" stroke="#fff" stroke-width=".8"/></svg>
        copperkettlecatering.example
      </span>
    </div>
  </section>

  <section class="card card--back">
    <div class="brand-name">Copper Kettle Catering</div>
    <p class="web-back">www.copperkettlecatering.example</p>
  </section>
</body>
</html>
```